Need Trifold Brochure

I need a trifold brochure asap for a project.

Please KNOW how to do a trifold brochure. It should be an 8 1/2 x 11 brochure that is folded in thirds. So there are ultimately 6 sections, 3 on the front and 3 on the back. We need content on both sides, not just one. If you aren't sure what a trifold is please google it. If you submit a design that is not a true trifold it will be immediately eliminated.

All content located on this page
http://harborviewcosmeticclinic.example/
All text on this page needs to be incorporated.

Also I attached the 3 before and after images. All 3 of these need to be incorporated preferable\y on the inside of the trifold on per page. The very BACK of the trifold doesn't have to have content, other than maybe the company and phone.

On the outside of the trifold (not the inside) you could do a muted sea or ocean scape as long as the text is legible.

Same colors as website.
Updates

Target Market(s)

See website. This is for face lifts, so mostly women age 40 and over.

Industry/Entity Type

It Company

Requirements
Must have
• All content located on this page

Also I attached the 3 before and after images. When the trifold is open these could be on each of the 3 pages of the trifold, preferably at the top.

Same colors as website.

```html
<!DOCTYPE html>
<html lang="en">
<head>
<meta charset="utf-8">
<title>The Evergreen Facelift – Trifold Brochure</title>
<link href="https://fonts.googleapis.com/css2?family=Source+Sans+3:wght@400;600;700&display=swap" rel="stylesheet">
<style>
  :root{
    --orange:#f37021;
    --sky:#8fb4ef;
    --navy:#1c2a8a;
    --ink:#3a3a3a;
    --frame:#9a9a9a;
    --paper:#ffffff;
    --stage:#e9ebee;
  }
  *{box-sizing:border-box;margin:0;padding:0}
  html,body{width:1200px;height:1000px;overflow:hidden}
  body{background:var(--stage);font-family:"Source Sans 3",Arial,sans-serif;color:var(--ink);position:relative}
  .spread{position:absolute;left:282px;width:636px;height:470px;display:flex;background:var(--paper);box-shadow:0 2px 10px rgba(0,0,0,.18)}
  .spread--inside{top:15px}
  .spread--outside{top:505px}
  .panel{position:relative;width:212px;height:100%;overflow:hidden}
  .panel + .panel{border-left:1px solid #e2e2e2}

  /* inside */
  .panel-band{position:absolute;left:0;right:0;bottom:0;height:82px;background:var(--sky)}
  .panel-band::before{content:"";position:absolute;left:0;right:0;top:0;height:6px;background:var(--navy)}
  .tab{position:absolute;top:14px;left:0;right:0;height:26px;background:var(--orange);color:#fff;font-weight:700;display:flex;align-items:center;justify-content:center;font-size:13px;white-space:nowrap}
  .tab--lead{justify-content:flex-start;padding-left:12px;font-size:15px}
  .tab--note{font-weight:400;font-size:9.5px}
  .photo{position:absolute;left:16px;width:180px;height:155px;border:3px solid var(--frame);border-radius:3px;z-index:2}
  .photo--before{top:52px}
  .photo--after{top:268px}
  .photo .label{position:absolute;right:6px;bottom:4px;font-size:9px;font-weight:700;color:#222;letter-spacing:.3px}
  .ph-a{background:linear-gradient(135deg,#cfd6df,#a98e80 60%,#6b5a55)}
  .ph-b{background:linear-gradient(135deg,#e8ebef,#c99a84 55%,#9c7460)}
  .ph-c{background:linear-gradient(135deg,#dfe3e8,#c19582 55%,#5a4a46)}
  .arrow{position:absolute;top:210px;left:16px;width:180px;height:50px;z-index:1}

  /* outside: offers */
  .offers{background:var(--sky)}
  .offers-sheet{position:absolute;left:14px;right:0;top:36px;height:240px;background:#fff}
  .offers h2{position:absolute;top:4px;left:14px;color:#fff;font-size:26px;font-weight:700;line-height:1}
  .offer-list{list-style:none;position:absolute;top:44px;left:22px;right:8px}
  .offer-list li{position:relative;padding-left:12px;font-size:8.6px;line-height:1.25;margin-bottom:4px;color:var(--ink)}
  .offer-list li::before{content:"";position:absolute;left:1px;top:3px;width:5px;height:5px;border:1px solid var(--sky);transform:rotate(45deg)}
  .offer-list b{color:var(--orange);font-weight:700}
  .offer-tag{position:absolute;top:280px;left:14px;right:0;text-align:center;color:var(--orange);font-weight:700;font-size:10.5px;line-height:1.25;background:#fff;padding:4px 0 6px}
  .total{position:absolute;top:318px;left:0;right:0;height:28px;background:var(--orange);color:#fff;display:flex;align-items:center;justify-content:center;gap:6px;font-weight:700;font-size:9px;letter-spacing:.5px}
  .total strong{font-size:18px}
  .call-block{position:absolute;top:354px;left:0;right:0;text-align:center;color:var(--navy);font-size:9.5px;line-height:1.25;text-transform:uppercase}
  .call-block .phone{font-weight:700}

  /* outside: back */
  .back-top{position:absolute;top:0;left:0;right:0;height:270px;background:linear-gradient(90deg,#b9b9b9,#eeeeee 45%,#ffffff 70%,#cfcfcf)}
  .back-info{position:absolute;top:282px;left:12px;right:10px}
  .back-info h3{color:var(--orange);font-size:15px;font-weight:700;margin-bottom:6px;white-space:nowrap}
  .back-info p{font-size:8.5px;line-height:1.45}
  .back-band{position:absolute;left:0;right:0;bottom:28px;height:14px;background:var(--navy)}

  /* outside: cover */
  .cover-scene{position:absolute;inset:0;background:linear-gradient(180deg,#2f6fc2 0%,#6aa0dd 30%,#c6dbf1 55%,#7f9fbf 66%,#8fb1cf 80%,#5f86ad 100%)}
  .cover-title{position:absolute;top:22px;left:0;right:0;text-align:center;color:#fff}
  .cover-title h1{font-size:18px;font-weight:700;white-space:nowrap}
  .cover-title p{font-size:10px;font-weight:600;line-height:1.25;margin-top:4px}
  .cover-band{position:absolute;left:0;right:0;bottom:0;height:62px;background:var(--sky);text-align:center;color:#fff;padding-top:16px}
  .cover-band::before{content:"";position:absolute;left:0;right:0;top:0;height:6px;background:var(--navy)}
  .cover-band .phone{font-size:13px;font-weight:700}
  .cover-band .web{font-size:8.5px;font-weight:700;color:var(--navy)}
</style>
</head>
<body>

<section class="spread spread--inside" aria-label="Brochure inside">
  <div class="panel">
    <div class="tab tab--lead">The Evergreen Facelift</div>
    <div class="photo photo--before ph-a" role="img" aria-label="Patient one before facelift, side profile"><span class="label">BEFORE</span></div>
    <svg class="arrow" viewBox="0 0 180 50" aria-hidden="true"><polygon points="0,0 180,0 180,18 90,48 0,18" fill="#9b9b9b"/></svg>
    <div class="photo photo--after ph-a" role="img" aria-label="Patient one after facelift, side profile"><span class="label">AFTER</span></div>
    <div class="panel-band"></div>
  </div>
  <div class="panel">
    <div class="tab">All are Actual Patients</div>
    <div class="photo photo--before ph-b" role="img" aria-label="Patient two before facelift, three-quarter view"><span class="label">BEFORE</span></div>
    <svg class="arrow" viewBox="0 0 180 50" aria-hidden="true"><polygon points="0,0 180,0 180,18 90,48 0,18" fill="#9b9b9b"/></svg>
    <div class="photo photo--after ph-b" role="img" aria-label="Patient two after facelift, three-quarter view"><span class="label">AFTER</span></div>
    <div class="panel-band"></div>
  </div>
  <div class="panel">
    <div class="tab tab--note">Patients also had optional neck lift procedure</div>
    <div class="photo photo--before ph-c" role="img" aria-label="Patient three before facelift and neck lift, side profile"><span class="label">BEFORE</span></div>
    <svg class="arrow" viewBox="0 0 180 50" aria-hidden="true"><polygon points="0,0 180,0 180,18 90,48 0,18" fill="#9b9b9b"/></svg>
    <div class="photo photo--after ph-c" role="img" aria-label="Patient three after facelift and neck lift, side profile"><span class="label">AFTER</span></div>
    <div class="panel-band"></div>
  </div>
</section>

<section class="spread spread--outside" aria-label="Brochure outside">
  <div class="panel offers">
    <div class="offers-sheet"></div>
    <h2>Offers</h2>
    <ul class="offer-list">
      <li><b>No</b> General Anesthesia<br>(but available as an option if desired)</li>
      <li><b>Decreased</b> Risks</li>
      <li><b>Less</b> Scars</li>
      <li><b>Very Quick</b> Recovery*</li>
      <li><b>Less</b> Bruising and Swelling*</li>
      <li><b>Significant</b> Improvement*</li>
      <li><b>No</b> Need for Special Post-Op Care</li>
      <li><b>Short</b> Surgery Time</li>
      <li><b>Free</b> Consultation With Our Staff</li>
      <li>Surgery performed by a fully ABPS Board Certified, internationally known, plastic surgeon.</li>
      <li>Optional add-on procedures can be done at the same time.</li>
    </ul>
    <p class="offer-tag">The new way to look<br>and feel better fast for less!</p>
    <div class="total">TOTAL COST <strong>$4500</strong></div>
    <p class="call-block">Call <span class="phone">555-014-0125</span><br>today for an appointment<br>in Bayview Heights<br>Harborview Cosmetic Clinic</p>
  </div>

  <div class="panel back">
    <div class="back-top"></div>
    <div class="back-info">
      <h3>The Evergreen Facelift</h3>
      <p>Address, ABC Street<br>XYZ lane, 123, Sampletown, UK<br>T : 555-014-0125<br>E : name@harborview.example<br>W : www.harborviewcosmeticclinic.example</p>
    </div>
    <div class="back-band"></div>
  </div>

  <div class="panel cover">
    <div class="cover-scene" role="img" aria-label="Muted seascape with blue sky, light clouds and calm water"></div>
    <div class="cover-title">
      <h1>The Evergreen Facelift</h1>
      <p>The new way to look<br>and feel better fast for less!</p>
    </div>
    <div class="cover-band">
      <div class="phone">Call : 555-014-0125</div>
      <div class="web">www.harborviewcosmeticclinic.example</div>
    </div>
  </div>
</section>

</body>
</html>
```